Email Banner for Technology Company

We need a new email banner. The purpose of the email banner is to make us look more professional as a business and keep all communications with clients uniform. The previous designs which we have included below have now become outdated as our brand has developed and we need the new banner to become more aligned and modern.

We are a marketing organization that specialises in lead generation, email newsletters are sent to prospects on a regular basis. Therefore, it is important that we have an aesthetically pleasing banner as this is the first real impression prospects have our business. First impressions matter.

We are looking for a new email banner design as the current design is now outdated and does not reflect who we are as a business.

The new banners are required for launch at the start of Q2.

There is future work in the pipeline for the winning design. We have multiple industry sites that will require the new design as well as creating each of these in multiple languages.

The design must include the Zevomarkly wording the tagline 'The Ultimate Research Library for Technology Pro's.
It needs to be creative and fun but still remain professional, sticking with the colour theme that already exists.

Requirements
Must have
• The design must include the Zevomarkly wording the tagline 'The Ultimate Research Library for Technology Pro's.

```html
<!DOCTYPE html>
<html lang="en">
<head>
<meta charset="utf-8">
<title>Zevomarkly Email Banner</title>
<link rel="stylesheet" href="https://fonts.googleapis.com/css2?family=Poppins:wght@500&display=swap">
<style>
  :root {
    --navy: #0c1f3c;
    --blue: #2e8fd0;
    --white: #ffffff;
  }
  html, body {
    margin: 0;
    padding: 0;
    width: 1200px;
    height: 191px;
    overflow: hidden;
    background: var(--white);
  }
  .banner {
    position: relative;
    width: 1200px;
    height: 191px;
    overflow: hidden;
    font-family: "Poppins", sans-serif;
    font-weight: 500;
    color: var(--white);
  }
  .banner-shapes {
    position: absolute;
    inset: 0;
    display: block;
  }
  .brand-name {
    position: absolute;
    left: 47px;
    top: 52px;
    margin: 0;
    font-size: 44px;
    line-height: 1;
    letter-spacing: -0.5px;
    font-weight: 500;
  }
  .tagline {
    position: absolute;
    left: 465px;
    top: 50px;
    margin: 0;
    font-size: 41px;
    line-height: 52px;
    font-weight: 500;
    white-space: nowrap;
  }
  .tagline-rule {
    position: absolute;
    left: 922px;
    top: 125px;
    width: 186px;
    height: 3px;
    background: var(--navy);
  }
</style>
</head>
<body>
  <div class="banner">
    <svg class="banner-shapes" width="1200" height="191" viewBox="0 0 1200 191" aria-hidden="true">
      <rect x="0" y="0" width="1200" height="191" fill="var(--navy)"/>
      <polygon class="divider-stripe" points="397,0 419,0 347,191 325,191" fill="var(--white)"/>
      <polygon class="tagline-panel" points="419,13 1200,13 1200,178 352,178" fill="var(--blue)"/>
    </svg>
    <div role="img" aria-label="Subtle hexagon network pattern over the navy and blue panels" style="position:absolute;inset:0;"></div>

    <p class="brand-name">Zevomarkly</p>

    <h1 class="tagline">The Ultimate Research Library<br>for Technology Pro's</h1>
    <span class="tagline-rule"></span>
  </div>
</body>
</html>
```